Influencer for sustainable living needs Youtube banner.

We are launching a Youtube Channel called "Reachable Greenhearth With Dorian Palk" and need a Youtube design banner that will represent the channel's theme, branding, and content. The size of the banner must be 2560 x 1440 pixels with an optimized area of 1546 x 423 pixels that views well on all device types.

The banner needs to have the title of the channel, the subline of the types of content (Tours | DIY Guides | Inspiration), and display Dorian Palk or his face. I have attached a picture of Dorian. We are open to using it as is or stylized.

The 3 types of Pillar content on the channel are:
1) Tours of sustainable properties and homes.
2) DIY educational and instructional videos.
3) Inspirational talks and interviews on sustainability and Permaculture.

The main purpose of the channel is to build our larger audience, increase trust and authority, and direct traffic to our paid educational offerings. Our paid educational offerings are hosted at “ReachableGreenhearthSchool.example”. Click through the website to better understand our branding & offerings. (Brand Manual and logo also attached)

The "influencer" is the founder of the School - Dorian Palk. He is a passionate, charismatic, and cheerful personality, who believes in the potential of humanity to create landscapes that thrive, so we can thrive within them. His core message is that humans can prove they are not a parasite by getting their homes, gardens, and communities in order so they shelter and feed us.

Files attached include versions of our logo and a branding manual for the School (note: the branding manual does not need to be followed exactly as it for the School (ReachableGreenhearthSchool.example) and not the Youtube channel (Reachable Greenhearth With Dorian Palk)... but the youtube channel branding should be similar.

DIYers, home owners, property owners, sustainable minded people, gardeners, homesteaders

Education, Sustainable living, Permaculture, Lifestyle

• Roboto & Urbanist. See design manual.

• Clean and bright design. Not cliche. Use of colours, fonts, and more from brand manual.
• I would like to see banner which compares to other professional youtubers.

```html
<!DOCTYPE html>
<html lang="en">
<head>
<meta charset="utf-8">
<title>Reachable Greenhearth With Dorian Palk — Channel Banner</title>
<link href="https://fonts.googleapis.com/css2?family=Caveat+Brush&family=Roboto:wght@500;700&family=Urbanist:wght@600&display=swap" rel="stylesheet">
<style>
  :root {
    --navy: #0b4161;
    --forest: #1f5a3a;
    --forest-dark: #123f35;
    --lime: #c2d82e;
    --lime-soft: #a9c23a;
    --teal: #5cc6b8;
    --white: #ffffff;
    --jacket: #2d476e;
  }
  * { margin: 0; padding: 0; box-sizing: border-box; }
  html, body { width: 1200px; height: 198px; overflow: hidden; background: var(--navy); }
  .banner {
    position: relative;
    width: 1200px;
    height: 198px;
    overflow: hidden;
    background: var(--navy);
  }
  .landscape-art {
    position: absolute;
    left: 0; top: 0;
    width: 600px; height: 198px;
    background: linear-gradient(90deg, var(--forest-dark) 0%, var(--forest) 45%, rgba(31,90,58,0.6) 80%, rgba(11,65,97,0) 100%);
  }
  .brand {
    position: absolute;
    left: 262px; top: 53px;
    display: flex;
    align-items: center;
    gap: 24px;
  }
  .brand-dot {
    width: 66px; height: 66px;
    border-radius: 50%;
    background: var(--lime);
  }
  .brand-name {
    font-family: "Urbanist", sans-serif;
    font-weight: 600;
    font-size: 34px;
    line-height: 36px;
    color: var(--white);
  }
  .title-joiner {
    position: absolute;
    left: 576px; top: 70px;
    font-family: "Caveat Brush", cursive;
    font-size: 34px;
    line-height: 36px;
    color: var(--lime);
  }
  .host-name {
    position: absolute;
    left: 658px; top: 46px;
    font-family: "Roboto", sans-serif;
    font-weight: 700;
    font-size: 45px;
    line-height: 52px;
    color: var(--white);
    letter-spacing: -0.3px;
  }
  .host-name .surname { color: var(--lime); }
  .content-band {
    position: absolute;
    left: 642px; top: 96px;
  }
  .content-list {
    position: absolute;
    left: 661px; top: 102px;
    font-family: "Roboto", sans-serif;
    font-weight: 500;
    font-size: 19.5px;
    line-height: 24px;
    color: var(--navy);
    white-space: nowrap;
  }
  .accent-shapes { position: absolute; right: 0; top: 0; }
  .host-photo {
    position: absolute;
    left: 940px; top: 6px;
    width: 196px; height: 192px;
    border-radius: 90px 90px 0 0;
    background: linear-gradient(180deg, #6b5a4e 0%, #4a4f63 40%, var(--jacket) 70%, #233a5c 100%);
  }
</style>
</head>
<body>
  <div class="banner">
    <div class="landscape-art" role="img" aria-label="Watercolour illustration of green rolling hills with trees and a farmhouse"></div>

    <div class="brand">
      <span class="brand-dot"></span>
      <div class="brand-name">Reachable<br>Greenhearth</div>
    </div>

    <span class="title-joiner">with</span>

    <h1 class="host-name">Dorian <span class="surname">Palk</span></h1>

    <svg class="content-band" width="340" height="42" viewBox="0 0 340 42" aria-hidden="true">
      <path d="M6 6 Q120 0 330 4 Q340 20 332 36 Q160 42 10 36 Q0 20 6 6 Z" fill="var(--teal)"/>
    </svg>
    <p class="content-list">Tours | DIY Guides | Inspiration</p>

    <svg class="accent-shapes" width="280" height="198" viewBox="0 0 280 198" aria-hidden="true">
      <path d="M30 0 H280 V198 H120 Q90 150 110 100 Q60 60 30 0 Z" fill="var(--teal)"/>
      <path d="M128 0 H280 V198 H160 Q150 150 175 110 Q150 60 128 0 Z" fill="var(--lime-soft)"/>
    </svg>

    <div class="host-photo" role="img" aria-label="Photo of the host Dorian Palk smiling, wearing a navy jacket"></div>
  </div>
</body>
</html>
```